Peanut Butter for Dogs - Label

Dear Designers,

Our company develops natural & innovative products aimed at enhancing animal (cat & dog) well-being. The company focuses on producing high-end, ethically sourced products that naturally soothe pets, improving their quality of life.

We are currently developing a new CBD-enriched Peanut Butter product for dogs, and we are looking for some label designs that follow our brand image & brand identity.

-> Please see full brief PDF file attached.

Target Market(s)

European Market (French Speaking)

Industry/Entity Type

Pet Food

Font styles to use
Other font styles liked:
• Please see brand kit in PDF brief

Colors

Designer to choose colors to be used in the design.

Requirements
Must have
• Please see brief PDF file attached
Nice to have
Should not have

```html
<!DOCTYPE html>
<html lang="fr">
<head>
<meta charset="utf-8">
<title>Calme Gourmand – Instructions</title>
<link rel="stylesheet" href="https://fonts.googleapis.com/css2?family=Arimo:wght@400;700&family=Montserrat:wght@500;600;700;800&family=Lora:wght@400&display=swap">
<style>
  :root {
    --ink: #141414;
    --teal: #3a9a7e;
    --teal-dark: #2f7f67;
    --grey-text: #3d3d3d;
    --soft-mint: #e9f0ed;
    --jar-edge: #d9dcdb;
    --jar-fill: #f4f5f5;
    --lid: #121212;
    --paper: #ffffff;
  }
  * { margin: 0; padding: 0; box-sizing: border-box; }
  html, body { width: 1200px; height: 1000px; overflow: hidden; background: var(--paper); }
  .slide { position: relative; width: 1200px; height: 1000px; overflow: hidden; background: var(--paper); font-family: "Arimo", Arial, sans-serif; color: var(--ink); }
  .corner-shape { position: absolute; }
  .corner-shape--top { left: 0; top: 0; }
  .corner-shape--bottom { right: 0; bottom: 0; }

  .slide-kicker { position: absolute; left: 36px; top: 64px; font-family: "Montserrat", sans-serif; font-weight: 600; font-size: 27px; letter-spacing: 3px; }
  .slide-title { position: absolute; left: 34px; top: 100px; font-family: "Montserrat", sans-serif; font-weight: 600; font-size: 62px; letter-spacing: 2px; }

  .brand { position: absolute; display: flex; align-items: center; gap: 8px; color: #1f3a2f; }
  .brand__dot { width: 12px; height: 12px; border-radius: 50%; background: var(--teal); }
  .brand__name { font-family: "Lora", serif; font-weight: 400; }
  .brand--header { right: 26px; top: 66px; }
  .brand--header .brand__name { font-size: 22px; }

  .brief { position: absolute; left: 58px; top: 258px; font-size: 23px; line-height: 35px; }
  .brief h2 { font-size: 23px; font-weight: 700; }
  .brief ul { list-style: none; }
  .brief li { position: relative; padding-left: 38px; }
  .brief li::before { content: "-"; position: absolute; left: 0; }
  .brief ul ul li { padding-left: 36px; margin-left: 26px; }
  .brief strong { font-weight: 700; }
  .brief__note { margin-top: 24px; }
  .brief__note p { line-height: 35px; }

  .jar { position: absolute; left: 664px; top: 392px; width: 426px; height: 540px; }
  .jar__lid { position: absolute; left: 0; top: 0; width: 426px; height: 94px; background: var(--lid); border-radius: 16px 16px 8px 8px; }
  .jar__body { position: absolute; left: 4px; top: 86px; width: 418px; height: 450px; background: var(--jar-fill); border: 2px solid var(--jar-edge); border-radius: 6px 6px 26px 26px; }

  .label { position: absolute; left: 668px; top: 528px; width: 420px; height: 330px; }
  .brand--label { left: 8px; top: 44px; }
  .brand--label .brand__name { font-size: 20px; color: var(--grey-text); }
  .label__title { position: absolute; left: 7px; top: 92px; font-family: "Montserrat", sans-serif; font-weight: 800; font-size: 40px; color: var(--teal); line-height: 1; }
  .label__subtitle { position: absolute; left: 8px; top: 134px; font-family: "Montserrat", sans-serif; font-weight: 700; font-size: 21px; color: var(--grey-text); letter-spacing: 0.5px; }
  .label__rule { position: absolute; left: 8px; width: 126px; height: 3px; background: var(--teal); }
  .label__rule--top { top: 190px; }
  .label__rule--bottom { top: 238px; }
  .label__cbd { position: absolute; left: 8px; top: 202px; font-family: "Montserrat", sans-serif; font-weight: 700; font-size: 18px; color: var(--grey-text); }
  .label__cbd span { color: var(--teal); }
  .label__audience { position: absolute; left: 6px; top: 252px; display: flex; align-items: center; gap: 6px; font-size: 13px; line-height: 15px; color: var(--teal); }
  .label__audience-icon { width: 40px; height: 30px; background: var(--teal); opacity: 0.85; border-radius: 4px; }
  .label__photo { position: absolute; right: 0; top: 128px; width: 186px; height: 182px; border-radius: 120px 0 0 120px; background: radial-gradient(circle at 55% 45%, #f3efe9, #d9d2c8); border: 6px solid var(--teal); border-right: none; }
  .label__band { position: absolute; left: 0; top: 310px; width: 420px; height: 18px; background: var(--teal); color: var(--paper); font-family: "Montserrat", sans-serif; font-weight: 700; font-size: 10px; line-height: 18px; text-align: center; letter-spacing: 0.3px; }
</style>
</head>
<body>
<main class="slide">
  <svg class="corner-shape corner-shape--top" width="300" height="250" viewBox="0 0 300 250" aria-hidden="true">
    <path d="M0 0 H300 C230 60 130 160 0 240 Z" fill="var(--soft-mint)"/>
  </svg>
  <svg class="corner-shape corner-shape--bottom" width="240" height="140" viewBox="0 0 240 140" aria-hidden="true">
    <path d="M240 0 V140 H0 C80 100 160 40 240 0 Z" fill="var(--soft-mint)"/>
  </svg>

  <p class="slide-kicker">SPECIFIC</p>
  <h1 class="slide-title">INSTRUCTIONS (1/3)</h1>

  <div class="brand brand--header">
    <span class="brand__dot"></span>
    <span class="brand__name">VERDELIA</span>
  </div>

  <section class="brief">
    <h2>Text elements to include (front of label):</h2>
    <ul>
      <li><strong>Product title:</strong> “Calme Gourmand”</li>
      <li><strong>CBD content:</strong> “CBD 150 MG”</li>
      <li><strong>Unique selling propositions:</strong>
        <ul>
          <li>“Anti-Stress”</li>
          <li>“100% naturel”</li>
          <li>“A lécher”</li>
          <li>“Beurre de cacahuète”</li>
        </ul>
      </li>
    </ul>
    <div class="brief__note">
      <h2>Important note:</h2>
      <p>People need to understand (visually)<br>this is a product for DOGS.</p>
    </div>
  </section>

  <div class="jar" aria-hidden="true">
    <div class="jar__body"></div>
    <div class="jar__lid"></div>
  </div>

  <section class="label">
    <div class="brand brand--label">
      <span class="brand__dot"></span>
      <span class="brand__name">VERDELIA</span>
    </div>
    <p class="label__title">CALME</p>
    <p class="label__subtitle">GOURMAND</p>
    <div class="label__rule label__rule--top"></div>
    <p class="label__cbd"><span>CBD</span> 150 MG</p>
    <div class="label__rule label__rule--bottom"></div>
    <div class="label__audience">
      <span>Pour<br>Chiens</span>
      <div class="label__audience-icon" role="img" aria-label="Silhouette d'un chien et d'un chat"></div>
    </div>
    <div class="label__photo" role="img" aria-label="Photo d'un bouledogue qui tire la langue"></div>
    <p class="label__band">ANTI-STRESS • 100% NATUREL • A LÉCHER • BEURRE DE CACAHUÈTE</p>
  </section>
</main>
</body>
</html>
```